gift box for organic and natural food items

My brand name is Tiller's Pantry and we are selling organic dried food to Korea now. We focus on transparent from the family farm to the customer directly with the single or simple organic ingredient. Our main customers are mainly woman from 30 to 50 years old. We have 4 different products for this package. Organic dried cherry, Organic dried figs, Organic dried dates and Organic dried pistachio. I would like to make a gift box that woman want to have and hold our natural products. The material of the gift box will be Royal Ivory Paper.

Target Market(s)

We will sell these items and gift box at the luxury department store.

Industry/Entity Type

Food Production

Font styles to use
Serif
Script

Colors
9ccb3b

Requirements
Must have
• Our slogan: A gift from the farm brought fresh to your door
• Our producer image: I will upload our producer's image
• We focus on the transparent and our producers.
• I will provide you with the image file for the only producers later.
Nice to have
• Brand logo / Our brand introduction sentences / NAFB logo / Color
• Color : Green & Bright Beige
• "Indulge. Nourish. Enjoy"
• "Taste the difference.
• The difference is quality.
• Quality you can experience"
• "As you savor the farm fresh delicacies enclosed in every box, relish in the fact that each ingredient was meticulously selected and directly sourced from hard working family farms. The result is a snacking experience like none other. With quality you can taste, our organic treats boast a unique flavor that will tantalize the taste buds. "
• "Upgrade your nourishment.
• Upgrade your nutrition.
• Upgrade your snack."
Should not have
• Too complicated with many colors

```html
<!DOCTYPE html>
<html lang="en">
<head>
<meta charset="utf-8">
<title>Tiller's Pantry — Gift Box Front</title>
<link rel="stylesheet" href="https://fonts.googleapis.com/css2?family=Didact+Gothic&family=Roboto+Condensed:wght@300&display=swap">
<style>
  :root {
    --backdrop: #8aeaf0;
    --leaf-green: #9ccb3b;
    --deep-green: #6c943a;
    --brand-green: #3f9160;
    --ink-green: #4d8c5c;
    --paper: #ffffff;
    --paper-shade: #dcdcdc;
    --rule-grey: #c9c9c9;
  }
  * { box-sizing: border-box; margin: 0; padding: 0; }
  html, body { width: 900px; height: 1200px; overflow: hidden; }
  body {
    background: var(--backdrop);
    font-family: "Didact Gothic", sans-serif;
    position: relative;
  }
  .gift-box {
    position: absolute;
    left: 150px;
    top: 70px;
    width: 600px;
    height: 1060px;
  }
  .box-front {
    position: absolute;
    left: 0; top: 0;
    width: 600px; height: 1060px;
    background: linear-gradient(180deg, var(--paper) 35%, var(--paper-shade) 100%);
    overflow: hidden;
  }
  .green-sweep {
    position: absolute;
    inset: 0;
    width: 600px; height: 1060px;
  }
  .lid-flap {
    position: absolute;
    left: -10px; top: 0;
    width: 620px; height: 270px;
    background: var(--paper);
    border-radius: 0 0 44px 44px;
    box-shadow: 0 10px 18px rgba(0,0,0,0.18);
    overflow: hidden;
  }
  .lid-band {
    position: absolute;
    left: 230px; top: 0;
    width: 200px; height: 270px;
    background: var(--leaf-green);
  }
  .handle-slot {
    position: absolute;
    left: 210px; top: 68px;
    width: 240px; height: 90px;
    border-radius: 45px;
    background: var(--backdrop);
  }
  .lid-pin {
    position: absolute;
    top: 195px;
    width: 9px; height: 9px;
    border-radius: 50%;
    background: #3f9aa0;
  }
  .lid-pin.left { left: 268px; }
  .lid-pin.right { left: 385px; }

  .brand-block {
    position: absolute;
    left: 40px; top: 335px;
    display: flex;
    align-items: center;
    gap: 14px;
  }
  .brand-dot {
    width: 34px; height: 34px;
    border-radius: 50%;
    background: var(--leaf-green);
  }
  .brand-name {
    font-family: "Didact Gothic", sans-serif;
    font-size: 58px;
    color: var(--brand-green);
    line-height: 1;
  }
  .slogan-band {
    position: absolute;
    left: 40px; top: 440px;
    padding: 6px 12px;
    background: var(--brand-green);
    color: var(--paper);
    font-family: "Roboto Condensed", sans-serif;
    font-weight: 300;
    font-size: 20px;
    letter-spacing: -0.3px;
    white-space: nowrap;
  }
  .quality-quote {
    position: absolute;
    left: 40px; top: 500px;
    font-size: 22px;
    line-height: 40px;
    color: var(--ink-green);
    letter-spacing: 0.5px;
  }
  .producers-portraits {
    position: absolute;
    left: 10px; top: 780px;
    width: 560px; height: 200px;
    background: linear-gradient(180deg, rgba(150,150,150,0.15) 0%, rgba(110,110,110,0.55) 100%);
    border-radius: 70px 70px 0 0;
  }
  .base-rule {
    position: absolute;
    left: 0; top: 985px;
    width: 600px; height: 6px;
    background: var(--rule-grey);
  }
  .base-band {
    position: absolute;
    left: 0; top: 991px;
    width: 600px; height: 69px;
    background: linear-gradient(90deg, var(--leaf-green), var(--deep-green));
  }
  .cert-badge {
    position: absolute;
    left: 520px; top: 990px;
    width: 56px; height: 56px;
    border-radius: 50%;
    background: var(--paper);
    border: 4px solid var(--brand-green);
  }
</style>
</head>
<body>
  <div class="gift-box">
    <div class="box-front">
      <svg class="green-sweep" viewBox="0 0 600 1060" aria-hidden="true">
        <defs>
          <linearGradient id="sweepFill" x1="0" y1="0" x2="1" y2="1">
            <stop offset="0" stop-color="#9ccb3b"/>
            <stop offset="1" stop-color="#6c943a"/>
          </linearGradient>
        </defs>
        <polygon points="600,250 600,1060 160,1060 240,930 420,560 560,290" fill="url(#sweepFill)"/>
        <path d="M470 420 L540 330 L548 336 L480 428 Z" fill="#9ccb3b"/>
        <path d="M400 620 L455 540 L462 546 L408 626 Z" fill="#9ccb3b"/>
      </svg>

      <div class="brand-block">
        <span class="brand-dot"></span>
        <span class="brand-name">Tiller's Pantry</span>
      </div>

      <div class="slogan-band">A gift from the farm brought fresh to your door</div>

      <p class="quality-quote">
        "Taste the difference.<br>
        The difference is quality.<br>
        Quality you can experience"
      </p>

      <div class="producers-portraits" role="img" aria-label="Pencil-style portraits of the four family farm producers"></div>

      <div class="base-rule"></div>
      <div class="base-band"></div>
      <div class="cert-badge" role="img" aria-label="Organic certification badge"></div>
    </div>

    <div class="lid-flap">
      <div class="lid-band"></div>
      <div class="handle-slot"></div>
      <span class="lid-pin left"></span>
      <span class="lid-pin right"></span>
    </div>
  </div>
</body>
</html>
```